Powerpoint template for Tolva - Helping people when they need it the most

Our most urgent need is a powerpoint template with logo, but over time we will also need web design, business card design etc.

We are Tolva Ventures AS, a company delivering innovative services for people when they need it the most.

Our first service, EaseBox (EaseBox by Tolva Ventures), will help people get through all the paperwork and obstacles they meet when they become seriously ill or loose someone close to them. This could typically be automation and digital handling of social security forms, insurance and banking etc.This will free up time for people to focus on recovery or spend time with family.

Our core values are: "Passionate", "Caring" and "Make a difference".
Our vision is (in Norwegian): «EaseBox hjelper deg når du trenger det som mest” which means "EaseBox is there for you when you need it the most".

We need a simple and pure design that:
- Signals to end-users that we are there to help them.
- Signals to investors that Tolva is an innovative company with services based on the latest technology.

The design should include an appropriate logo.
We would like a warm color to be used (we have been using red until now).

Check out our website for more background information: www.tolva-example.no

See also the attached homemade powerpoint presentation that we need to turn into a spectacular pitch! Please do NOT keep much from the original slides.

Target Market(s)

Keep in mind that we are a Scandinavian company.
We want a simple, warm/caring and innovative design that also conveys our tech side.

Industry/Entity Type

Business

Requirements
Must have
• Pictures (of people) - This is all about people
• For our investor pitch we will eventually need slides regarding
• - The problem
• - Our insight / domain knowledge
• - Product/Solution/How it works
• - Vision
• - Market/ Market size / Market potential
• - Business Model
• - Competition / Competetive advantages
• - Plan / Milestones / Timeline
• - The team
• - Strength & weaknesses (including network)
• - Investors / Partners
• - Value proposition
• - Elevator pitch
• - Why Invest (What's in it for the investor)
• - Concerns & Responses
• - Tolva in numbers
• - Financials
• - Q& A
• The slides should reflect that we see ourselves as a tech company (although a caring one) as machine learning, artificial intelligence and robotics.
• In the phase we are in right now we will be interviewing lots of potential users to understand the underlying needs. It would be good to have some pictures to illustrate the interview and user testing situations.
• These are just tips for you to understand what we are occupied with. Please feel free to use you're creativity!
Should not have
• Very bright and exotic colors. We are a Nordic/Scandinavian company

```html
<!DOCTYPE html>
<html lang="no">
<head>
<meta charset="utf-8">
<title>EaseBox by Tolva Ventures – presentation template</title>
<link rel="stylesheet" href="https://fonts.googleapis.com/css2?family=Anton&family=Open+Sans:wght@400;600;700&display=swap">
<style>
:root{
  --red:#e10600;
  --black:#111111;
  --white:#ffffff;
  --board:#cbcbcb;
  --ink:#222222;
  --muted:#666666;
}
*{box-sizing:border-box;margin:0;padding:0}
html,body{width:1200px;height:797px;overflow:hidden}
body{background:var(--board);position:relative;font-family:"Open Sans",Arial,sans-serif;color:var(--ink)}
.slide{position:absolute;width:550px;height:310px;background:var(--white);overflow:hidden;box-shadow:0 1px 4px rgba(0,0,0,.25)}
.slide svg.shapes{position:absolute;left:0;top:0}
.slide-label{position:absolute;width:550px;text-align:center;font-size:24px;letter-spacing:.5px;color:var(--black)}
.cover{left:32px;top:32px}
.pitch{left:615px;top:32px}
.idea{left:32px;top:410px}
.team{left:615px;top:410px}

.display{font-family:"Anton",Impact,sans-serif;font-weight:400}
.red{color:var(--red)}
.footer-url{position:absolute;left:0;right:0;bottom:15px;display:flex;justify-content:center;align-items:center;gap:8px;font-size:5.5px;letter-spacing:3px;color:#444}
.footer-url::before,.footer-url::after{content:"";width:30px;height:1px;background:#888}
.page-no{position:absolute;right:16px;bottom:15px;font-size:5.5px;color:#444}
.corner{position:absolute;bottom:0;width:38px;height:36px;background:var(--red)}
.corner.left{left:0;clip-path:polygon(0 0,100% 100%,0 100%)}
.corner.right{right:0;clip-path:polygon(100% 0,100% 100%,0 100%)}
.logo-box{position:absolute;border:1.5px solid var(--black);font-family:"Anton",Impact,sans-serif;color:var(--black);display:flex;align-items:center;justify-content:center;background:var(--white);letter-spacing:.3px}

/* cover */
.cover-title{position:absolute;top:14px;left:0;right:0;text-align:center;font-size:35px;line-height:1;letter-spacing:.3px;color:var(--black)}
.cover-photo{position:absolute;left:0;top:68px;width:550px;height:194px;background:linear-gradient(100deg,#b9b4ab 0%,#e7e8ea 35%,#9a9ea2 60%,#d9dde0 100%)}
.cover .logo-box{left:224px;top:149px;width:116px;height:41px;font-size:22px}

/* pitch */
.section-title{position:absolute;font-family:"Open Sans",Arial,sans-serif;font-weight:700;color:var(--black)}
.pitch .section-title{left:19px;top:20px;font-size:13px}
.pitch .title-rule{position:absolute;left:0;top:37px;width:123px;height:1px;background:var(--red)}
.pitch .logo-box{left:479px;top:17px;width:55px;height:18px;font-size:10px}
.pitch-text{position:absolute;top:222px;width:110px;text-align:center;font-size:6px;line-height:1.35;color:var(--ink)}

/* idea */
.idea .logo-box{left:479px;top:18px;width:55px;height:18px;font-size:10px}
.idea .section-title{left:274px;top:62px;font-size:13.5px;border-bottom:1px solid var(--red);padding-bottom:1px}
.idea-list{position:absolute;left:275px;top:105px;width:252px;list-style:none}
.idea-list li{position:relative;padding-left:14px;font-size:6.6px;line-height:1.5;margin-bottom:25px;text-align:justify}
.idea-list svg{position:absolute;left:0;top:1px}

/* team */
.team .logo-box{left:218px;top:23px;width:116px;height:40px;font-size:22px}
.team-band{position:absolute;left:0;top:86px;width:550px;height:92px;background:var(--red);color:var(--white);text-align:center;padding:6px 40px 0}
.team-band h2{font-weight:400;font-size:13px;margin-bottom:5px}
.team-band p{font-size:5.3px;line-height:1.4;margin-bottom:6px}
.contact-call{position:absolute;top:199px;left:0;right:0;text-align:center;font-size:13px;font-weight:600;color:var(--black)}
.contact-line{position:absolute;left:0;right:0;text-align:center;font-size:5.8px;color:var(--ink);display:flex;justify-content:center;align-items:center;gap:4px}
</style>
</head>
<body>

<!-- Cover -->
<section class="slide cover">
  <h1 class="cover-title display"><span class="red">EASEBOX</span> BY TOLVA <span class="red">VENTURES</span></h1>
  <div class="cover-photo" role="img" aria-label="Photo of an elderly man with a walking stick on a snowy winding road"></div>
  <svg class="shapes" width="550" height="310" viewBox="0 0 550 310">
    <defs><clipPath id="coverClip"><rect x="0" y="68" width="550" height="194"/></clipPath></defs>
    <g clip-path="url(#coverClip)">
      <polygon points="300,58 408,165 300,272 192,165" fill="#ffffff" opacity=".35"/>
      <polygon points="274,58 381,165 274,272 167,165" fill="#ffffff"/>
    </g>
  </svg>
  <div class="logo-box">LOGO HERE</div>
  <div class="footer-url">www.tolva-example.no</div>
  <div class="corner left"></div><div class="corner right"></div>
</section>
<div class="slide-label" style="left:32px;top:355px">COVER PAGE</div>

<!-- Page 01 -->
<section class="slide pitch">
  <h2 class="section-title"><span class="red">ELEVATOR</span> PITCH</h2>
  <div class="title-rule"></div>
  <div class="logo-box">LOGO HERE</div>
  <svg class="shapes" width="550" height="310" viewBox="0 0 550 310">
    <g id="pitch-item-1">
      <polyline points="77,92 52,120 77,148" fill="none" stroke="var(--red)" stroke-width="2.5"/>
      <polyline points="133,92 158,120 133,148" fill="none" stroke="var(--red)" stroke-width="2.5"/>
      <rect x="63" y="78" width="84" height="84" rx="9" transform="rotate(45 105 120)" fill="var(--black)"/>
      <circle cx="105" cy="120" r="20" fill="var(--red)"/>
      <text x="105" y="129" text-anchor="middle" font-family="Open Sans,Arial,sans-serif" font-weight="700" font-size="24" fill="var(--black)">?</text>
      <circle cx="105" cy="173" r="2.5" fill="var(--red)"/>
      <line x1="105" y1="175" x2="105" y2="206" stroke="var(--red)" stroke-width="1" stroke-dasharray="2 2"/>
      <circle cx="105" cy="207" r="2.5" fill="var(--red)"/>
    </g>
    <g id="pitch-item-2">
      <polyline points="249,92 224,120 249,148" fill="none" stroke="var(--red)" stroke-width="2.5"/>
      <polyline points="305,92 330,120 305,148" fill="none" stroke="var(--red)" stroke-width="2.5"/>
      <rect x="235" y="78" width="84" height="84" rx="9" transform="rotate(45 277 120)" fill="var(--black)"/>
      <circle cx="277" cy="120" r="20" fill="var(--red)"/>
      <circle cx="273" cy="123" r="6" fill="none" stroke="var(--black)" stroke-width="3.5" stroke-dasharray="2.2 1.6"/>
      <circle cx="273" cy="123" r="2" fill="var(--black)"/>
      <circle cx="282" cy="115" r="4" fill="none" stroke="var(--black)" stroke-width="2.5" stroke-dasharray="1.6 1.2"/>
      <circle cx="277" cy="173" r="2.5" fill="var(--red)"/>
      <line x1="277" y1="175" x2="277" y2="206" stroke="var(--red)" stroke-width="1" stroke-dasharray="2 2"/>
      <circle cx="277" cy="207" r="2.5" fill="var(--red)"/>
    </g>
    <g id="pitch-item-3">
      <polyline points="421,92 396,120 421,148" fill="none" stroke="var(--red)" stroke-width="2.5"/>
      <polyline points="477,92 502,120 477,148" fill="none" stroke="var(--red)" stroke-width="2.5"/>
      <rect x="407" y="78" width="84" height="84" rx="9" transform="rotate(45 449 120)" fill="var(--black)"/>
      <circle cx="449" cy="120" r="20" fill="var(--red)"/>
      <rect x="446" y="109" width="6" height="22" fill="var(--black)"/>
      <rect x="438" y="117" width="22" height="6" fill="var(--black)"/>
      <circle cx="449" cy="173" r="2.5" fill="var(--red)"/>
      <line x1="449" y1="175" x2="449" y2="206" stroke="var(--red)" stroke-width="1" stroke-dasharray="2 2"/>
      <circle cx="449" cy="207" r="2.5" fill="var(--red)"/>
    </g>
  </svg>
  <p class="pitch-text" style="left:50px">EaseBox hjelper deg når du trenger det som mest.</p>
  <p class="pitch-text" style="left:217px;width:120px">EaseBox løser etterlattes og alvorlig sykes utfordringer ved å ordne opp i økonomiske og praktiske ordninger.</p>
  <p class="pitch-text" style="left:397px;width:104px">Slik kan familien bruke kreftene på å leve videre eller bli friske igjen.</p>
  <div class="footer-url">www.tolva-example.no</div>
  <div class="page-no">01</div>
  <div class="corner left"></div><div class="corner right"></div>
</section>
<div class="slide-label" style="left:615px;top:355px">PAGE - 01</div>

<!-- Page 02 -->
<section class="slide idea">
  <svg class="shapes" width="550" height="310" viewBox="0 0 550 310">
    <defs>
      <linearGradient id="carePhoto" x1="0" y1="0" x2="0" y2="1">
        <stop offset="0" stop-color="#e9dcae"/>
        <stop offset=".55" stop-color="#c9b57a"/>
        <stop offset="1" stop-color="#6f8a3a"/>
      </linearGradient>
    </defs>
    <polygon points="0,0 68,0 205,155 40,310 0,310" fill="var(--red)"/>
    <polyline points="120,0 268,155 120,310" fill="none" stroke="var(--red)" stroke-width="1.6"/>
    <rect x="79" y="102" width="106" height="106" rx="12" transform="rotate(45 132 155)" fill="var(--black)"/>
    <g role="img" aria-label="Photo of a carer pushing an elderly person in a wheelchair through a sunny field">
      <rect x="31" y="83" width="142" height="142" rx="16" transform="rotate(45 102 154)" fill="url(#carePhoto)"/>
    </g>
  </svg>
  <div class="logo-box">LOGO HERE</div>
  <h2 class="section-title"><span class="red">FORRETNINGSIDÉEN –</span> HVA SKAL LØSES?</h2>
  <ul class="idea-list">
    <li><svg width="8" height="8" viewBox="0 0 8 8"><circle cx="4" cy="4" r="3.3" fill="none" stroke="var(--red)" stroke-width=".9"/><polyline points="2.3,4 3.6,5.3 6.6,1.8" fill="none" stroke="var(--red)" stroke-width="1.1"/></svg>Med forankring i vår innsikt, er alt det praktiske som må ordnes, et enormt problem for mange mennesker som står i en livskrise.</li>
    <li><svg width="8" height="8" viewBox="0 0 8 8"><circle cx="4" cy="4" r="3.3" fill="none" stroke="var(--red)" stroke-width=".9"/><polyline points="2.3,4 3.6,5.3 6.6,1.8" fill="none" stroke="var(--red)" stroke-width="1.1"/></svg>Vi vil hjelpe mennesker til heller å bruke tid og krefter på det som er viktigst her i livet – være sammen med sine nærmeste.</li>
    <li><svg width="8" height="8" viewBox="0 0 8 8"><circle cx="4" cy="4" r="3.3" fill="none" stroke="var(--red)" stroke-width=".9"/><polyline points="2.3,4 3.6,5.3 6.6,1.8" fill="none" stroke="var(--red)" stroke-width="1.1"/></svg>Vi vil øke livskvaliteten ved å gi en mindre bekymringsfull alderdom / sykdom – sikret praktisk hjelp, enten til seg selv eller til de etterlatte.</li>
  </ul>
  <div class="footer-url">www.tolva-example.no</div>
  <div class="page-no">02</div>
  <div class="corner right"></div>
</section>
<div class="slide-label" style="left:32px;top:740px">PAGE - 02</div>

<!-- Back page -->
<section class="slide team">
  <div class="logo-box">LOGO HERE</div>
  <div class="team-band">
    <h2>TEAM TOLVA</h2>
    <p>We are two girls who are genuinely concerned about the opportunities technology provides for simplifying people's everyday lives. By finding the intersection of physical and digital that provides good user experiences, we can add real and meaningful value to our customers and users. Our background is from the finance industry with expertise from business development, project management, sales management and technology.</p>
    <p>We are in Bergen and Oslo.</p>
    <p>Team Tolva participates in the incentive program, Fjord Challenge, to the Fjord Hub.<br>In addition, Team Tolva also participates in the startup investment program, Nordlys Challenge, for Startup Nordlys Challenge.</p>
  </div>
  <div class="contact-call"><span class="red">CALL US TODAY</span>&nbsp; (+47) 40000123</div>
  <div class="contact-line" style="top:223px">
    <svg width="5" height="7" viewBox="0 0 5 7"><path d="M2.5 0C1.1 0 0 1.1 0 2.5 0 4.3 2.5 7 2.5 7S5 4.3 5 2.5C5 1.1 3.9 0 2.5 0Zm0 3.4a.9.9 0 1 1 0-1.8.9.9 0 0 1 0 1.8Z" fill="var(--black)"/></svg>
    Tolva Ventures AS Company No. 900000000
  </div>
  <div class="contact-line" style="top:237px">
    <svg width="6" height="5" viewBox="0 0 6 5"><rect width="6" height="5" fill="var(--black)"/><polyline points="0,0 3,2.6 6,0" fill="none" stroke="#fff" stroke-width=".6"/></svg>
    hello@tolva-example.no
  </div>
  <div class="footer-url">www.tolva-example.no</div>
  <div class="corner left"></div><div class="corner right"></div>
</section>
<div class="slide-label" style="left:615px;top:740px">BACK PAGE</div>

</body>
</html>
```